Stationery/business card design for "Mobile Echoscan Partners LLC"
Mobile Echoscan Partners, LLC
Professional
Tariq Velmont, RDMS
Director of Operations
27836 Brevard Lane,
Cypress, Texas, 70318
info@mobileechoscanpartners.example
www.mobileechoscanpartners.example
There will be two names on the business cards. The names and titles are the following;
Farida Kostral
Sales and Marketing
This is the logo design

```html
<!DOCTYPE html>
<html lang="en">
<head>
<meta charset="utf-8">
<title>Mobile Echoscan Partners, LLC — Stationery</title>
<link rel="stylesheet" href="https://fonts.googleapis.com/css2?family=Montserrat:wght@500;600;700&family=Open+Sans:wght@400;600&display=swap">
<style>
:root{
  --bg:#2a2b2d;
  --paper:#ffffff;
  --brand:#2f7db3;
  --brand-dark:#1f5f8e;
  --sweep:#e5e8eb;
  --ink:#3a3f45;
  --muted:#8a9099;
  --rule:#c9ced4;
}
*{box-sizing:border-box;margin:0;padding:0}
html,body{width:1200px;height:754px;overflow:hidden;background:var(--bg)}
body{position:relative;font-family:"Open Sans",Arial,sans-serif;color:var(--ink)}
.piece{position:absolute;background:var(--paper);overflow:hidden;box-shadow:0 6px 18px rgba(0,0,0,.35)}
.band{position:absolute;left:0;bottom:0;width:100%;display:block}
.brand-mark{display:flex;align-items:center;gap:6px;font-family:"Montserrat",Arial,sans-serif;font-weight:700;color:var(--brand);line-height:1.1}
.brand-mark .dot{width:14px;height:14px;border-radius:50%;background:var(--brand);flex:none}
.brand-mark.light{color:#fff}
.brand-mark.light .dot{background:#fff}
.band-text{position:absolute;left:0;right:0;text-align:center;color:#fff;font-size:6.5px;letter-spacing:.3px}

/* letterhead */
.letterhead{left:60px;top:48px;width:300px;height:424px}
.letterhead .brand-mark{position:absolute;top:26px;left:0;right:0;justify-content:center;font-size:9px}
.letterhead .band{height:90px}
.letterhead .band-text{bottom:14px}

/* fax sheet */
.fax-sheet{left:392px;top:48px;width:300px;height:424px}
.fax-sheet .brand-mark{position:absolute;top:26px;left:0;right:0;justify-content:center;font-size:9px}
.fax-title{position:absolute;top:72px;right:26px;font-family:"Montserrat",Arial,sans-serif;font-weight:700;font-size:13px;letter-spacing:1px;color:var(--ink)}
.fax-table{position:absolute;top:94px;left:26px;right:26px;border-collapse:collapse;font-size:7px;color:var(--muted)}
.fax-table td{border:1px solid var(--rule);height:16px;padding:0 5px}
.fax-table td.label{width:44px;font-weight:600;color:var(--ink)}
.fax-sheet .band{height:90px}
.fax-sheet .band-text{bottom:14px}

/* envelope */
.envelope{left:724px;top:48px;width:416px;height:208px}
.envelope .flap{position:absolute;inset:0;width:100%;height:100%}
.envelope .brand-mark{position:absolute;top:132px;left:0;right:0;justify-content:center;font-size:10px}

/* note card */
.note-card{left:724px;top:282px;width:416px;height:190px}
.note-card .brand-mark{position:absolute;top:22px;left:22px;font-size:9px;width:150px}
.note-card .band{height:70px}

/* business cards */
.biz-card{top:508px;width:300px;height:172px;border-radius:10px}
.card-front{left:60px;background:var(--brand)}
.card-front .brand-mark{position:absolute;top:30px;left:26px;font-size:12px;width:210px}
.card-front .contact{position:absolute;left:26px;bottom:24px;color:#fff;font-size:8px;line-height:1.6}
.card-back{left:392px}
.card-back .brand-mark{position:absolute;top:20px;left:22px;font-size:9px;width:170px}
.card-back .person{position:absolute;top:70px;left:22px}
.person-name{font-family:"Montserrat",Arial,sans-serif;font-weight:600;font-size:12px;color:var(--brand-dark)}
.person-title{font-size:8px;color:var(--muted);margin-top:2px}
.card-back .band{height:44px}

.card-back-alt{left:724px}
</style>
</head>
<body>

<section class="piece letterhead" aria-label="Letterhead">
  <div class="brand-mark"><span class="dot"></span>Mobile Echoscan Partners, LLC</div>
  <svg class="band" viewBox="0 0 300 90" preserveAspectRatio="none" aria-hidden="true">
    <path d="M0 22 Q140 -6 300 14 L300 90 L0 90Z" fill="var(--sweep)"/>
    <path d="M0 40 Q150 8 300 32 L300 90 L0 90Z" fill="var(--brand)"/>
  </svg>
  <p class="band-text">27836 Brevard Lane, Cypress, Texas, 70318 &nbsp;|&nbsp; info@mobileechoscanpartners.example &nbsp;|&nbsp; www.mobileechoscanpartners.example</p>
</section>

<section class="piece fax-sheet" aria-label="Fax cover sheet">
  <div class="brand-mark"><span class="dot"></span>Mobile Echoscan Partners, LLC</div>
  <p class="fax-title">FAX</p>
  <table class="fax-table">
    <tr><td class="label">To</td><td></td><td class="label">From</td><td></td></tr>
    <tr><td class="label">Fax</td><td></td><td class="label">Date</td><td></td></tr>
    <tr><td class="label">Pages</td><td></td><td class="label">Re</td><td></td></tr>
  </table>
  <svg class="band" viewBox="0 0 300 90" preserveAspectRatio="none" aria-hidden="true">
    <path d="M0 22 Q140 -6 300 14 L300 90 L0 90Z" fill="var(--sweep)"/>
    <path d="M0 40 Q150 8 300 32 L300 90 L0 90Z" fill="var(--brand)"/>
  </svg>
  <p class="band-text">27836 Brevard Lane, Cypress, Texas, 70318 &nbsp;|&nbsp; info@mobileechoscanpartners.example &nbsp;|&nbsp; www.mobileechoscanpartners.example</p>
</section>

<section class="piece envelope" aria-label="Envelope">
  <svg class="flap" viewBox="0 0 416 208" preserveAspectRatio="none" aria-hidden="true">
    <path d="M0 0 L208 118 L416 0" fill="none" stroke="var(--rule)" stroke-width="1.2"/>
    <path d="M0 208 L170 100 M416 208 L246 100" fill="none" stroke="var(--rule)" stroke-width="1"/>
  </svg>
  <div class="brand-mark"><span class="dot"></span>Mobile Echoscan Partners, LLC</div>
</section>

<section class="piece note-card" aria-label="Note card">
  <div class="brand-mark"><span class="dot"></span>Mobile Echoscan Partners, LLC</div>
  <svg class="band" viewBox="0 0 416 70" preserveAspectRatio="none" aria-hidden="true">
    <path d="M0 18 Q200 -6 416 12 L416 70 L0 70Z" fill="var(--sweep)"/>
    <path d="M0 34 Q210 6 416 28 L416 70 L0 70Z" fill="var(--brand)"/>
  </svg>
</section>

<section class="piece biz-card card-front" aria-label="Business card front">
  <div class="brand-mark light"><span class="dot"></span>Mobile Echoscan Partners, LLC</div>
  <div class="contact">
    27836 Brevard Lane, Cypress, Texas, 70318<br>
    info@mobileechoscanpartners.example<br>
    www.mobileechoscanpartners.example
  </div>
</section>

<section class="piece biz-card card-back" aria-label="Business card back">
  <div class="brand-mark"><span class="dot"></span>Mobile Echoscan Partners, LLC</div>
  <div class="person">
    <p class="person-name">Tariq Velmont, RDMS</p>
    <p class="person-title">Director of Operations</p>
  </div>
  <svg class="band" viewBox="0 0 300 44" preserveAspectRatio="none" aria-hidden="true">
    <path d="M0 12 Q150 -4 300 8 L300 44 L0 44Z" fill="var(--sweep)"/>
    <path d="M0 22 Q150 2 300 18 L300 44 L0 44Z" fill="var(--brand)"/>
  </svg>
</section>

<section class="piece biz-card card-back card-back-alt" aria-label="Business card back, second name">
  <div class="brand-mark"><span class="dot"></span>Mobile Echoscan Partners, LLC</div>
  <div class="person">
    <p class="person-name">Farida Kostral</p>
    <p class="person-title">Sales and Marketing</p>
  </div>
  <svg class="band" viewBox="0 0 300 44" preserveAspectRatio="none" aria-hidden="true">
    <path d="M0 12 Q150 -4 300 8 L300 44 L0 44Z" fill="var(--sweep)"/>
    <path d="M0 22 Q150 2 300 18 L300 44 L0 44Z" fill="var(--brand)"/>
  </svg>
</section>

</body>
</html>
```